Entertainment Sound and Lighting company Business card

We need a professional looking business card designed for my growing entertainment sound and lighting company based in Sydney, Australia called "Kestrel Sound"

We provide technical production services (sound systems/lighting/vision) for events ranging from band gigs, weddings, corporate functions etc.

The business card needs to contain the following information:

Bartholomew Quenneville
Audio Engineer
Phone: 0478 615 702
Email: bartholomew@kestrelsound.com.au
Website: www.kestrelsound.com.au

Business logo has been attached in .ai format, please contact me if you need me to provide other files.

Target Market(s)

We need a business card that reflects our modern and professional company but still looks professional to appeal to our corporate clients.
We have a very broad target market spanning from bands needing PA systems for their gigs (18-30yrs) to event companies needing sound and lighting for weddings and other functions.

Industry/Entity Type

Business

Requirements
Must have
• Needs to include the logo that is attached of course, and the colour scheme.
Nice to have
• - Double sided

```html
<!DOCTYPE html>
<html lang="en">
<head>
<meta charset="utf-8">
<title>Kestrel Sound — Business Card</title>
<link rel="stylesheet" href="https://fonts.googleapis.com/css2?family=Open+Sans:wght@400;600;700&display=swap">
<style>
  :root {
    --page-bg: #e4e4e4;
    --card-white: #ffffff;
    --blue-deep: #0a5cbf;
    --blue-bright: #2f97ec;
    --cyan: #4fe8f0;
    --brand-blue: #1a72d6;
    --text-light: #ffffff;
  }
  * { margin: 0; padding: 0; box-sizing: border-box; }
  html, body {
    width: 1001px;
    height: 1200px;
    overflow: hidden;
    background: var(--page-bg);
    font-family: "Open Sans", sans-serif;
  }
  .card {
    position: absolute;
    left: 85px;
    width: 831px;
    height: 472px;
    overflow: hidden;
  }
  .card--front {
    top: 68px;
    background: linear-gradient(135deg, var(--blue-deep) 0%, var(--blue-bright) 100%);
  }
  .card--back {
    top: 592px;
    background: var(--card-white);
  }
  .card__wave {
    position: absolute;
    inset: 0;
    width: 100%;
    height: 100%;
  }
  .brand {
    position: absolute;
    display: flex;
    align-items: center;
    gap: 14px;
    font-weight: 600;
    letter-spacing: -0.5px;
    line-height: 1;
    white-space: nowrap;
  }
  .brand__dot {
    width: 22px;
    height: 22px;
    border-radius: 50%;
    background: currentColor;
    flex: none;
  }
  .card--front .brand {
    right: 54px;
    bottom: 50px;
    font-size: 54px;
    color: var(--text-light);
  }
  .card--back .brand {
    right: 40px;
    top: 160px;
    font-size: 54px;
    color: var(--brand-blue);
  }
  .contact {
    position: absolute;
    left: 38px;
    top: 298px;
    color: var(--text-light);
  }
  .contact__name {
    font-size: 21px;
    font-weight: 400;
    line-height: 1.2;
  }
  .contact__name strong { font-weight: 600; }
  .contact__role {
    font-size: 15px;
    margin-top: 2px;
  }
  .contact__lines {
    list-style: none;
    margin-top: 22px;
    font-size: 19px;
    line-height: 28px;
  }
</style>
</head>
<body>
  <section class="card card--front" aria-label="Business card front">
    <div class="brand"><span class="brand__dot"></span>Kestrel Sound</div>
  </section>

  <section class="card card--back" aria-label="Business card back">
    <svg class="card__wave" viewBox="0 0 831 472" preserveAspectRatio="none" aria-hidden="true">
      <defs>
        <linearGradient id="waveFill" x1="0.15" y1="0" x2="0.75" y2="1">
          <stop offset="0" stop-color="#4fe8f0"/>
          <stop offset="0.45" stop-color="#1f8fe0"/>
          <stop offset="1" stop-color="#0a56b8"/>
        </linearGradient>
      </defs>
      <path d="M0,272 L106,172 C300,300 560,420 818,472 L0,472 Z" fill="url(#waveFill)"/>
    </svg>
    <div class="brand"><span class="brand__dot"></span>Kestrel Sound</div>
    <div class="contact">
      <p class="contact__name">Bartholomew <strong>Quenneville</strong></p>
      <p class="contact__role">Audio Engineer</p>
      <ul class="contact__lines">
        <li>0478.615.702</li>
        <li>bartholomew@kestrelsound.com.au</li>
        <li>www.kestrelsound.com.au</li>
      </ul>
    </div>
  </section>
</body>
</html>
```